Business Cards

Business cards (double-sided) to be handed out to clients and potential clients, with contact details, logo .

Target Market(s)

Small to medium size businesses

Industry/Entity Type

Accountants

Contact Information for Business Card

Brightwater Ledger & Counsel Ltd

Colors

Designer to choose only greyscale colors for use in the design.

Requirements
Must have
• Name, Title, Address, Phone number, Email, Website
Nice to have
• Modern, clean lines, classy
Should not have
• Business cards to be double-sided. Form keeps reverting to single-sided.

```html
<!DOCTYPE html>
<html lang="en">
<head>
<meta charset="utf-8">
<title>Brightwater Ledger & Counsel Ltd — Business Cards</title>
<link rel="stylesheet" href="https://fonts.googleapis.com/css2?family=Josefin+Sans:wght@400&family=Open+Sans:wght@700&display=swap">
<style>
  :root {
    --page: #ffffff;
    --front-top: #363c44;
    --front-mid: #1d2126;
    --front-bottom: #0a0b0c;
    --back-top: #f6f6f7;
    --back-mid: #ececed;
    --back-bottom: #d4d5d7;
    --ink-light: #ffffff;
    --ink-dark: #1e2124;
    --contact-ink: #33383d;
    --icon-disc: #353b40;
    --icon-mark: #ffffff;
  }
  * { box-sizing: border-box; margin: 0; padding: 0; }
  html, body {
    width: 1200px; height: 1200px; overflow: hidden;
    background: var(--page);
  }
  .canvas { position: relative; width: 1200px; height: 1200px; }

  .card { position: absolute; overflow: hidden; }
  .card-front { left: 205px; top: 83px; width: 780px; height: 469px; }
  .card-back { left: 198px; top: 597px; width: 787px; height: 489px; }

  .card-surface { position: absolute; inset: 0; }
  .card-front .card-surface {
    background: linear-gradient(180deg, var(--front-top) 0%, var(--front-mid) 45%, var(--front-bottom) 100%);
  }
  .card-back .card-surface {
    background: linear-gradient(160deg, var(--back-top) 0%, var(--back-mid) 45%, var(--back-top) 70%, var(--back-mid) 100%),
                linear-gradient(20deg, var(--back-bottom) 0%, transparent 40%);
    background-blend-mode: multiply;
  }

  .brand-name {
    position: absolute;
    font-family: "Josefin Sans", sans-serif;
    font-weight: 400;
    text-transform: uppercase;
    line-height: 1;
    text-align: left;
  }
  .brand-name .brand-primary { display: block; letter-spacing: 0.06em; }
  .brand-name .brand-secondary { display: block; letter-spacing: 0.16em; margin-top: 10px; }

  .card-front .brand-name {
    color: var(--ink-light);
    left: 50%; top: 50%;
    transform: translate(-50%, -50%);
  }
  .card-front .brand-primary { font-size: 38px; }
  .card-front .brand-secondary { font-size: 13px; }

  .card-back .brand-name {
    color: var(--ink-dark);
    left: 90px; top: 224px;
  }
  .card-back .brand-primary { font-size: 29px; }
  .card-back .brand-secondary { font-size: 10px; margin-top: 8px; }

  .contact-list { position: absolute; left: 453px; top: 144px; list-style: none; }
  .contact-item {
    position: absolute; left: 0;
    display: flex; align-items: center;
    width: 300px;
  }
  .contact-item:nth-child(1) { top: 0; }
  .contact-item:nth-child(2) { top: 64px; }
  .contact-item:nth-child(3) { top: 135px; }
  .contact-item:nth-child(4) { top: 198px; }

  .contact-icon { width: 42px; height: 42px; flex: none; }
  .contact-text {
    margin-left: 12px;
    font-family: "Open Sans", sans-serif;
    font-weight: 700;
    font-size: 11.5px;
    line-height: 16px;
    color: var(--contact-ink);
    text-transform: uppercase;
  }
</style>
</head>
<body>
<main class="canvas">

  <section class="card card-front" aria-label="Card front">
    <div class="card-surface" role="img" aria-label="Dark faceted diamond pattern background"></div>
    <h1 class="brand-name">
      <span class="brand-primary">Brightwater</span>
      <span class="brand-secondary">Ledger &amp; Counsel Ltd</span>
    </h1>
  </section>

  <section class="card card-back" aria-label="Card back">
    <div class="card-surface" role="img" aria-label="Light faceted diamond pattern background"></div>
    <h2 class="brand-name">
      <span class="brand-primary">Brightwater</span>
      <span class="brand-secondary">Ledger &amp; Counsel Ltd</span>
    </h2>

    <ul class="contact-list">
      <li class="contact-item">
        <svg class="contact-icon" viewBox="0 0 42 42" aria-hidden="true">
          <circle cx="21" cy="21" r="21" fill="var(--icon-disc)"/>
          <rect x="10" y="13.5" width="22" height="15" fill="none" stroke="var(--icon-mark)" stroke-width="1.8"/>
          <path d="M10 13.5 L21 23 L32 13.5 M10 28.5 L18 21 M32 28.5 L24 21" fill="none" stroke="var(--icon-mark)" stroke-width="1.6"/>
        </svg>
        <span class="contact-text">info@company-name</span>
      </li>
      <li class="contact-item">
        <svg class="contact-icon" viewBox="0 0 42 42" aria-hidden="true">
          <circle cx="21" cy="21" r="21" fill="var(--icon-disc)"/>
          <path d="M15 11 C13 12 12 14 12.5 16.5 C14 23 19 28 25.5 29.5 C28 30 30 29 31 27 L27.5 23.5 L24.5 25.5 C21 24 18 21 16.5 17.5 L18.5 14.5 Z" fill="var(--icon-mark)"/>
        </svg>
        <span class="contact-text">+01 2345 6789 0123<br>+09 8765 4321 0987</span>
      </li>
      <li class="contact-item">
        <svg class="contact-icon" viewBox="0 0 42 42" aria-hidden="true">
          <circle cx="21" cy="21" r="21" fill="var(--icon-disc)"/>
          <path d="M9 21 L21 11 L33 21" fill="none" stroke="var(--icon-mark)" stroke-width="2.4" stroke-linejoin="round"/>
          <path d="M13 20 L21 14 L29 20 L29 31 L24 31 L24 25 L18 25 L18 31 L13 31 Z" fill="var(--icon-mark)"/>
        </svg>
        <span class="contact-text">Your city address<br>Street location, state, country</span>
      </li>
      <li class="contact-item">
        <svg class="contact-icon" viewBox="0 0 42 42" aria-hidden="true">
          <circle cx="21" cy="21" r="21" fill="var(--icon-disc)"/>
          <circle cx="21" cy="21" r="10" fill="none" stroke="var(--icon-mark)" stroke-width="1.8"/>
          <path d="M15 15 C17 16 18 18 17 20 C16 22 18 23 19 25 L18 29 C14 27 12 23 13 18 Z M23 13 C25 14 27 16 26 18 C25 20 27 22 29 21 C30 24 28 27 25 29 C24 26 23 24 22 22 C21 19 22 16 23 13 Z" fill="var(--icon-mark)"/>
        </svg>
        <span class="contact-text">www.your-company-name</span>
      </li>
    </ul>
  </section>

</main>
</body>
</html>
```